Book cover for book about Climate Change

Looking for a clean, bold, and attractive cover for a mass-market paperback (5.5"x 8.5") about solving the climate change problem. Title is either "When Rivers Learn to Sing” or A Lantern Over Quiet Fields” (your choice), subtitle is "A five-step plan to reverse climate change — to ensure that your grandchildren will live on a clean and comfortable planet," author is Dale Pruitt. Thinking that it *might* feature an image of Earth (or a portion thereof) and its very thin layer of atmosphere -- but STRONGLY encourage other ideas too!

Requirements
Nice to have
• Keep it positive — NOT scary doom-and-gloom

```html
<!DOCTYPE html>
<html lang="en">
<head>
<meta charset="utf-8">
<title>A Lantern Over Quiet Fields — Cover</title>
<link rel="stylesheet" href="https://fonts.googleapis.com/css2?family=Bebas+Neue&family=Oswald:wght@300;400&display=swap">
<style>
  :root {
    --backdrop: #d8d8d8;
    --leaf-light: #a6e32c;
    --leaf-deep: #86cc1c;
    --night: #2a2a2a;
    --ink-light: #ffffff;
  }
  html, body {
    margin: 0;
    padding: 0;
    width: 1200px;
    height: 800px;
    overflow: hidden;
    background: var(--backdrop);
  }
  .canvas {
    position: relative;
    width: 1200px;
    height: 800px;
  }
  .cover {
    position: absolute;
    left: 340px;
    top: 30px;
    width: 520px;
    height: 740px;
    overflow: hidden;
    background: linear-gradient(180deg, var(--leaf-light) 0%, var(--leaf-deep) 60%);
    box-shadow: 0 6px 18px rgba(0,0,0,0.18);
  }
  .cover__title {
    position: absolute;
    top: 96px;
    left: 0;
    right: 0;
    margin: 0;
    text-align: center;
    color: var(--ink-light);
    font-family: "Bebas Neue", "Oswald", sans-serif;
    font-weight: 400;
    line-height: 1;
  }
  .cover__title-line {
    display: block;
    font-size: 62px;
    letter-spacing: 0.5px;
  }
  .cover__title-link {
    display: block;
    font-size: 22px;
    margin: 18px 0 18px;
  }
  .cover__scene {
    position: absolute;
    left: 0;
    top: 300px;
    width: 520px;
    height: 170px;
  }
  .cover__ground {
    position: absolute;
    left: 0;
    right: 0;
    top: 468px;
    bottom: 0;
    background: var(--night);
  }
  .cover__subtitle {
    position: absolute;
    top: 488px;
    left: 40px;
    right: 40px;
    margin: 0;
    text-align: center;
    color: var(--ink-light);
    font-family: "Oswald", sans-serif;
    font-weight: 300;
    font-size: 10.5px;
    line-height: 1.55;
    letter-spacing: 0.2px;
    text-transform: uppercase;
  }
  .cover__author {
    position: absolute;
    right: 20px;
    bottom: 22px;
    margin: 0;
    color: var(--ink-light);
    font-family: "Bebas Neue", "Oswald", sans-serif;
    font-size: 28px;
    letter-spacing: 0.5px;
  }
</style>
</head>
<body>
<main class="canvas">
  <section class="cover">
    <svg class="cover__scene" viewBox="0 0 520 170" role="img" aria-label="Silhouette of an acacia tree and a giraffe standing on a grassy hill at dusk">
      <defs>
        <linearGradient id="scene-fade" x1="0" y1="0" x2="0" y2="1">
          <stop offset="0" stop-color="#86cc1c" stop-opacity="0"/>
          <stop offset="0.55" stop-color="#4a6b1f" stop-opacity="0.6"/>
          <stop offset="1" stop-color="#2a2a2a"/>
        </linearGradient>
      </defs>
      <rect x="0" y="0" width="520" height="170" fill="url(#scene-fade)"/>
    </svg>

    <h1 class="cover__title">
      <span class="cover__title-line">A Lantern</span>
      <span class="cover__title-link">Over</span>
      <span class="cover__title-line">Quiet Fields</span>
    </h1>

    <div class="cover__ground"></div>

    <p class="cover__subtitle">A five-step plan to reverse climate change — to ensure that your grandchildren will<br>live on a clean and comfortable planet</p>

    <p class="cover__author">Dale Pruitt</p>
  </section>
</main>
</body>
</html>
```